Briskly Verdant Vessel Plots

We need a quillnet page designed that matches the logo on our business card (See separate brief on Pixel Harbor). We are a small business that design compact succulent gardens using our imagination to pair the natural qualities of the plants with their containers. Wherever possible we carefully select upcycled, quirky, vintage and recycled materials for our containers so that each piece is unique. Succulents require very little maintenance and in Spring and Summer will delight and suprise you with their unexpected and sometimes quite spectacular display of flowers. We also offer a small range of delightful individually handcrafted garden art windchimes and mobiles also made from carefully selected vintage items.
Contact Information : Message Me @ QN or email Moira via Briskly.Verdant@quenmail.example to arrange pick up and address details in Annerley Brisbane.

(CAN YOU PLEASE DELETE ANY PICS WHICH ARE BADLY OUT OF FOCUS - I HAVE A LOT OF TROUBLE WITH MY DSLR CAMERA AS MY EYES ARE GETTING BAD)

I would like the Echinevera Lilac Rose as our Logo if possible but the photo came from imagevault and should be attributed somewhere to "lanternfox."

thanks Moira

This project has been bundled with a Business Card Design Project: http://tasks.pixelharbor.example/task.aspx?id=517604

I encourage you to submit to both projects and keep designs consistent.

Target Market(s)

The target market is adults in South East Queensland aged 18 -75 looking for unusual and personalised gifts particularly for people who enjoy gardening or live in an apartment wth limited opportunity for gardening and those who appreciate vintage, quirky and upcycled things.

Industry/Entity Type

Small Business

Font styles to use
Script

Colors

Designer to choose colors to be used in the design.

Requirements
Must have

• I would like the Echinevera Lilac Rose as our Logo if possible but the photo came from imagevault and should be attributed somewhere to "lanternfox." This photo is in the bottom right hand corner.

The QN page must complement and be consistent with the "branding" on the business cards project.
Nice to have
• I quite like the script type of font but not too curly and feminine as this product has to appeal to men and women alike. So something a bit sophisticated but not "girly"

I quite like the second pic in the second row of the faces and curly tales and the first two shots in the bottom row should go on the QN page somewhere as a collection of current stock (though it is constantly growing - pardon the pun)
Should not have
• (CAN YOU PLEASE DELETE ANY PICS I have uploaded WHICH ARE BADLY OUT OF FOCUS - I HAVE A LOT OF TROUBLE WITH MY DSLR CAMERA AS MY EYES ARE GETTING BAD)

There are some minatures there which have been planted in corks and mounted on boards with stencil decorations - these obviously need to be turned around 90 degrees.

```html
<!DOCTYPE html>
<html lang="en">
<head>
<meta charset="utf-8">
<title>Briskly Verdant – quillnet page</title>
<link rel="stylesheet" href="https://fonts.googleapis.com/css2?family=Arimo:wght@400;700&family=Cormorant+Garamond:wght@400;500&display=swap">
<style>
  :root {
    --bar-blue: #3b5998;
    --bar-edge: #29487d;
    --page-bg: #e9eaed;
    --card-bg: #ffffff;
    --card-edge: #d3d6db;
    --text-main: #141823;
    --text-muted: #9197a3;
    --link-blue: #3b5998;
    --nav-muted: #9da7be;
    --button-bg: #f6f7f9;
    --button-edge: #ced0d4;
    --button-text: #4e5665;
    --cover-teal: #7fc9cf;
    --cover-lilac: #8f86b8;
    --cover-rose: #c97aa8;
    --cover-sand: #b39c86;
  }
  * { box-sizing: border-box; margin: 0; padding: 0; }
  html, body { width: 1200px; height: 690px; overflow: hidden; }
  body {
    position: relative;
    background: var(--page-bg);
    font-family: "Arimo", Helvetica, Arial, sans-serif;
    color: var(--text-main);
  }
  .abs { position: absolute; }

  /* top bar */
  .top-bar {
    left: 0; top: 0; width: 1200px; height: 44px;
    background: var(--bar-blue);
    border-bottom: 1px solid var(--bar-edge);
  }
  .network-name {
    left: 14px; top: 12px;
    color: #fff; font-size: 16px; font-weight: 700;
  }
  .search-box {
    left: 92px; top: 8px; width: 648px; height: 27px;
    background: #fff; border: 1px solid var(--bar-edge); border-radius: 2px;
    font-size: 15px; font-weight: 700; padding: 5px 8px;
  }
  .search-box svg { position: absolute; right: 7px; top: 4px; }
  .home-link {
    left: 1065px; top: 15px; color: #fff; font-size: 12.5px; font-weight: 700;
    padding-left: 9px; border-left: 1px solid #4e69a2; height: 17px;
  }
  .home-arrow { left: 1126px; top: 22px; }

  /* cover */
  .cover {
    left: 50px; top: 44px; width: 951px; height: 352px;
    background:
      radial-gradient(circle at 42% 40%, #a7e4e4 0%, var(--cover-teal) 16%, #6cb7c4 30%, var(--cover-lilac) 52%, var(--cover-rose) 68%, var(--cover-sand) 86%);
  }
  .cover-title {
    left: 711px; top: 240px; color: #fff;
    font-family: "Cormorant Garamond", Georgia, serif; font-weight: 500;
    font-size: 58px; line-height: 58px;
    text-shadow: 0 1px 3px rgba(0,0,0,.35);
  }
  .header-band {
    left: 50px; top: 396px; width: 951px; height: 85px;
    background: var(--card-bg); border: 1px solid var(--card-edge); border-top: none;
  }
  .profile-frame {
    left: 76px; top: 279px; width: 190px; height: 190px;
    background: #fff; border: 1px solid var(--button-edge); padding: 4px;
    box-shadow: 0 1px 2px rgba(0,0,0,.1);
  }
  .profile-photo {
    position: relative; width: 100%; height: 100%;
    background: radial-gradient(circle at 55% 38%, #a7e4e4 0%, var(--cover-teal) 30%, #5fa9b7 60%, var(--cover-lilac) 100%);
  }
  .profile-initials {
    position: absolute; left: 22px; bottom: 10px; color: #fff;
    font-family: "Cormorant Garamond", Georgia, serif; font-size: 40px;
  }
  .page-name {
    left: 291px; top: 333px; color: #fff; font-size: 27px; font-weight: 700;
    text-shadow: 0 1px 3px rgba(0,0,0,.6);
  }
  .page-category {
    left: 291px; top: 368px; color: #fff; font-size: 15.5px;
    text-shadow: 0 1px 2px rgba(0,0,0,.6);
  }
  .tabs { left: 276px; top: 408px; display: flex; height: 45px; }
  .tab {
    padding: 12px 17px 0; font-size: 15.5px; color: #4b4f56;
    border-right: 1px solid #e1e2e3; height: 37px; margin-top: 4px;
  }
  .tab:last-child { border-right: none; }
  .tab.is-active { font-weight: 700; color: var(--text-main); border-bottom: 3px solid #5890ff; border-bottom-color: var(--link-blue); }
  .tabs-rule { left: 276px; top: 452px; width: 414px; height: 4px; background: #e9eaed; }
  .page-button {
    top: 415px; height: 27px; background: var(--button-bg);
    border: 1px solid var(--button-edge); border-radius: 2px;
    font-size: 14px; font-weight: 700; color: var(--button-text);
    display: flex; align-items: center;
  }
  .like-button { left: 760px; width: 70px; padding-left: 8px; gap: 5px; }
  .message-button { left: 842px; width: 132px; }
  .message-button span { padding: 0 9px; border-right: 1px solid var(--button-edge); height: 100%; display: flex; align-items: center; }
  .message-button svg { margin-left: 9px; }

  /* right rail */
  .create-button {
    left: 1016px; top: 58px; width: 91px; height: 25px;
    background: #5b74a8; border: 1px solid #29447e; border-radius: 2px;
    color: #fff; font-size: 12.5px; font-weight: 700; text-align: center; line-height: 23px;
  }
  .rail-rule { left: 1010px; top: 97px; width: 190px; height: 1px; background: #d3d6db; }
  .year-nav { left: 1016px; top: 108px; list-style: none; }
  .year-nav li {
    height: 25.7px; line-height: 25.7px; padding-left: 12px;
    border-left: 3px solid #d8dde8; font-size: 12.5px; color: var(--nav-muted);
  }
  .year-nav li.is-current { border-left-color: var(--link-blue); color: var(--link-blue); font-weight: 700; }

  /* left column */
  .side-card {
    left: 50px; width: 367px; background: var(--card-bg);
    border: 1px solid var(--card-edge); border-radius: 3px;
  }
  .side-head {
    height: 41px; padding: 14px 12px; font-size: 12px; font-weight: 700;
    color: #4b4f56; border-bottom: 1px solid #e5e5e5; position: relative;
  }
  .side-head svg { position: absolute; right: 12px; top: 13px; }
  .people-card { top: 484px; height: 132px; }
  .like-count { text-align: center; font-size: 16px; color: var(--text-muted); padding: 16px 0 14px; border-bottom: 1px solid #e5e5e5; }
  .like-count b { color: var(--text-main); }
  .invite-link { font-size: 13.5px; color: var(--link-blue); padding: 12px 13px; }
  .about-card { top: 632px; height: 80px; }

  /* post */
  .post-card {
    left: 430px; top: 484px; width: 571px; height: 230px;
    background: var(--card-bg); border: 1px solid var(--card-edge); border-radius: 3px;
  }
  .post-avatar {
    position: absolute; left: 8px; top: 11px; width: 49px; height: 49px;
    background: radial-gradient(circle at 50% 50%, #9fbf8a 0%, #6f8f5e 35%, #b04f8b 75%);
  }
  .post-author { position: absolute; left: 68px; top: 18px; font-size: 13.5px; font-weight: 700; color: var(--link-blue); }
  .post-date { position: absolute; left: 68px; top: 37px; font-size: 13px; color: var(--text-muted); display: flex; gap: 6px; align-items: center; }
  .post-menu { position: absolute; right: 10px; top: 14px; }
  .post-body {
    position: absolute; left: 13px; top: 69px; width: 545px;
    font-size: 15.5px; line-height: 22.4px; color: var(--text-main);
  }
  .post-body a { color: var(--link-blue); text-decoration: none; }
</style>
</head>
<body>
  <header class="abs top-bar"></header>
  <div class="abs network-name">quillnet</div>
  <div class="abs search-box">Briskly Verdant
    <svg width="17" height="17" viewBox="0 0 17 17" aria-hidden="true"><circle cx="7" cy="7" r="5" fill="none" stroke="#4b4f56" stroke-width="2"/><line x1="10.5" y1="10.5" x2="15.5" y2="15.5" stroke="#4b4f56" stroke-width="2.2"/></svg>
  </div>
  <div class="abs home-link">Home</div>
  <svg class="abs home-arrow" width="9" height="6" viewBox="0 0 9 6" aria-hidden="true"><path d="M0 0h9L4.5 5z" fill="#fff"/></svg>

  <div class="abs cover" role="img" aria-label="Cover photo: close-up of a lilac rose echeveria rosette with teal leaves and pink edges"></div>
  <div class="abs cover-title">Briskly<br>Verdant</div>
  <div class="abs header-band"></div>

  <div class="abs profile-frame">
    <div class="profile-photo" role="img" aria-label="Profile photo: lilac rose echeveria rosette">
      <span class="profile-initials">BV</span>
    </div>
  </div>
  <div class="abs page-name">Briskly Verdant</div>
  <div class="abs page-category">Local Business</div>

  <nav class="abs tabs">
    <div class="tab is-active">Timeline</div>
    <div class="tab">About</div>
    <div class="tab">Photos</div>
    <div class="tab">Likes</div>
    <div class="tab">Videos</div>
  </nav>
  <div class="abs tabs-rule"></div>

  <div class="abs page-button like-button">
    <svg width="14" height="13" viewBox="0 0 14 13" aria-hidden="true"><path d="M1 6h3v7H1zM5 6l3-6c1.5 0 2 1 1.6 2.5L9 5h4c.8 0 1.2.7 1 1.4l-1.5 5.5c-.2.7-.7 1.1-1.4 1.1H5z" fill="none" stroke="#4e5665" stroke-width="1.2"/></svg>
    Like
  </div>
  <div class="abs page-button message-button">
    <span>Message</span>
    <svg width="28" height="12" viewBox="0 0 28 12" aria-hidden="true"><circle cx="6" cy="6" r="3.3" fill="none" stroke="#4e5665" stroke-width="2.4" stroke-dasharray="2 1.5"/><circle cx="6" cy="6" r="1.2" fill="#4e5665"/><path d="M17 4h8l-4 5z" fill="#4e5665"/></svg>
  </div>

  <div class="abs create-button">Create Page</div>
  <div class="abs rail-rule"></div>
  <ul class="abs year-nav">
    <li class="is-current">Now</li>
    <li>October</li>
    <li>2012</li>
    <li>2011</li>
    <li>Founded</li>
  </ul>

  <section class="abs side-card people-card">
    <div class="side-head">PEOPLE
      <svg width="9" height="14" viewBox="0 0 9 14" aria-hidden="true"><path d="M1.5 1.5l5.5 5.5-5.5 5.5" fill="none" stroke="#4b4f56" stroke-width="2"/></svg>
    </div>
    <div class="like-count"><b>14</b> likes</div>
    <div class="invite-link">Invite your friends to like this Page</div>
  </section>
  <section class="abs side-card about-card">
    <div class="side-head">ABOUT
      <svg width="9" height="14" viewBox="0 0 9 14" aria-hidden="true"><path d="M1.5 1.5l5.5 5.5-5.5 5.5" fill="none" stroke="#4b4f56" stroke-width="2"/></svg>
    </div>
  </section>

  <article class="abs post-card">
    <div class="post-avatar" role="img" aria-label="Page thumbnail: succulent arrangement in a star-shaped container"></div>
    <div class="post-author">Briskly Verdant</div>
    <div class="post-date">November 23
      <svg width="11" height="11" viewBox="0 0 11 11" aria-hidden="true"><circle cx="5.5" cy="5.5" r="5" fill="#b0b5bd"/></svg>
    </div>
    <svg class="post-menu" width="12" height="8" viewBox="0 0 12 8" aria-hidden="true"><path d="M1 1l5 5 5-5" fill="none" stroke="#c4c7cc" stroke-width="1.6"/></svg>
    <p class="post-body">Today was the first day of trading at the Kestrel Flats Markets - well the 4.30am start on a Sunday morning was definitely a shock to the system but we were soon upacking our products and setting up our stall. What an extraordinary experience to watch so many early birds rushing about looking to catch their particular worms. While I couldnt claim that we had the most successful trading day- we did rec... <a href="#">See More</a></p>
  </article>
</body>
</html>
```